푸른들누리회는 한결행정부 산하 공공기관으로, 근로여건 및 소득수준이 상대적으로 열악하고 고용이 불안정한 건설근로자들간의 상호부조 및 복리증진을 도모하고 노후생활 안정을 위하여 설립된 기관입니다.
누리회의 사업은 크게 공제부금 수납, 공제부금 운용, 퇴직공제금 지급, 고용.복지 서비스 제공 등으로 구성됩니다.
공제부금 수납은 퇴직공제 가입 사업장으로부터 근로자의 근로일수에 상응하는 공제부금을 수납하는 과정이고, 공제부금 운용은 피공제자에게 지급할 퇴직공제금을 더 많이 그리고 안정적으로 지급할 수 있도록 적립된 공제부금을 불리고 관리하는 과정입니다.
이렇게 축적된 돈을 활용하여 퇴직공제금(퇴직금)을 지급하거나 고용.복지 서비스를 제공합니다. 복지 서비스로는 결혼,출산 보조금 지원, 자녀 교육비 지원, 근로자 건강검진 등이 있으며 고용 서비스로는 건설근로자의 숙련도를 높여주는 기능훈련사업, 무료로 구인자와 구직자를 매개하는 취업지원사업이 있습니다.

```html
<!DOCTYPE html>
<html lang="ko">
<head>
<meta charset="utf-8">
<title>건설근로자들의 행복온도 높이기</title>
<link href="https://fonts.googleapis.com/css2?family=Noto+Sans+KR:wght@400;500;700;900&display=swap" rel="stylesheet">
<style>
  :root {
    --page: #ecebe8;
    --paper: #ffffff;
    --ink: #2f2f2f;
    --orange: #e9862a;
    --orange-deep: #d9701c;
    --green: #8cc43e;
    --green-deep: #6ea52a;
    --tan: #d6a45a;
    --teal: #3f9c93;
    --sky: #5b8fd0;
    --card: #ffffff;
    --muted: #6b6b6b;
  }
  * { box-sizing: border-box; margin: 0; padding: 0; }
  html, body { width: 1200px; height: 1200px; overflow: hidden; }
  body {
    background: var(--page);
    font-family: "Noto Sans KR", sans-serif;
    color: var(--ink);
  }
  .poster {
    position: absolute;
    left: 175px; top: 0;
    width: 850px; height: 1200px;
    background: var(--paper);
    overflow: hidden;
  }
  .brand-top {
    position: absolute; left: 42px; top: 34px;
    display: flex; align-items: center; gap: 8px;
    font-size: 17px; font-weight: 700; color: var(--ink);
  }
  .brand-dot { width: 18px; height: 18px; border-radius: 50%; background: var(--green); }
  .headline {
    position: absolute; left: 120px; top: 118px;
    font-weight: 900; font-size: 60px; line-height: 1.22; letter-spacing: -2px;
    color: var(--ink);
  }
  .headline .hot { color: var(--orange); }
  .headline .warm { color: var(--green-deep); }
  .scene-art {
    position: absolute; left: 330px; top: 90px;
    width: 490px; height: 400px;
    background:
      radial-gradient(circle at 72% 20%, #6f9ee0 0 13%, transparent 14%),
      radial-gradient(circle at 30% 45%, #e7a63c 0 15%, transparent 16%),
      radial-gradient(circle at 78% 52%, #e05f2c 0 14%, transparent 15%),
      radial-gradient(circle at 40% 78%, #58a79b 0 14%, transparent 15%),
      radial-gradient(circle at 66% 82%, #bfc6c9 0 12%, transparent 13%),
      linear-gradient(180deg, #ffffff 0%, #f6efe4 100%);
    border-radius: 8px;
  }
  .ground {
    position: absolute; left: 0; top: 440px; width: 850px; height: 130px;
  }
  .about {
    position: absolute; left: 0; top: 552px; width: 850px; height: 648px;
    background: var(--green);
    padding: 0 64px;
  }
  .about-title {
    margin-top: 92px;
    font-size: 30px; font-weight: 900; color: #fff; letter-spacing: -1px;
  }
  .about-text {
    margin-top: 14px;
    font-size: 15.5px; line-height: 1.6; color: #fff; font-weight: 500;
  }
  .biz-title {
    margin-top: 40px;
    font-size: 24px; font-weight: 900; color: var(--ink);
  }
  .biz-list {
    margin-top: 14px;
    display: grid; grid-template-columns: repeat(5, 1fr); gap: 14px;
  }
  .biz-card {
    background: var(--card); border-radius: 6px; overflow: hidden;
    height: 206px; text-align: center;
    box-shadow: 0 2px 0 rgba(0,0,0,0.08);
  }
  .biz-name {
    background: var(--orange); color: #fff;
    font-size: 13.5px; font-weight: 700; letter-spacing: -0.5px;
    padding: 8px 4px;
  }
  .biz-icon {
    width: 56px; height: 56px; margin: 16px auto 12px;
    border-radius: 50%; background: #f3f0ea;
    display: flex; align-items: center; justify-content: center;
  }
  .biz-desc {
    font-size: 12px; line-height: 1.55; color: var(--muted); padding: 0 12px;
  }
  .footer {
    position: absolute; left: 64px; right: 64px; bottom: 38px;
    border-top: 2px solid rgba(255,255,255,0.6);
    padding-top: 20px;
    display: flex; justify-content: space-between; align-items: center;
  }
  .contact { font-size: 15px; color: var(--ink); line-height: 1.7; font-weight: 500; }
  .contact b { font-weight: 700; margin-right: 10px; }
  .contact .sep { display: inline-block; width: 2px; height: 13px; background: var(--ink); margin-right: 10px; vertical-align: -1px; }
  .brand-foot {
    display: flex; align-items: center; gap: 10px;
    font-size: 26px; font-weight: 700; color: #fff;
  }
  .brand-foot .brand-dot { width: 28px; height: 28px; background: var(--orange); }
</style>
</head>
<body>
<main class="poster">
  <div class="brand-top"><span class="brand-dot"></span>푸른들누리회</div>

  <h1 class="headline">건설근로자들의<br><span class="hot">행복</span><span class="warm">온도</span><br>높이기</h1>

  <div class="scene-art" role="img" aria-label="건설근로자들이 퍼즐 조각을 맞추는 일러스트: 퇴직공제금, 생활안정자금 대부, 복지서비스, 취업지원, 기능향상 훈련 퍼즐"></div>

  <svg class="ground" viewBox="0 0 850 130" preserveAspectRatio="none" aria-hidden="true">
    <path d="M0 78 C120 78 200 78 250 60 C280 48 300 40 340 40 L850 40 L850 130 L0 130 Z" fill="var(--tan)"/>
  </svg>

  <section class="about">
    <h2 class="about-title">푸른들누리회란?</h2>
    <p class="about-text">근로여건 및 소득수준이 상대적으로 열악하고 고용이 불안정한<br>건설근로자의 고용개선과 복지향상을 위해 1997년 설립된 한결행정부 산하 공공기관입니다.</p>

    <h3 class="biz-title">주요사업</h3>
    <div class="biz-list">
      <article class="biz-card">
        <div class="biz-name">퇴직공제금 지급</div>
        <div class="biz-icon"><svg width="30" height="30" viewBox="0 0 30 30"><circle cx="15" cy="15" r="11" fill="none" stroke="var(--orange)" stroke-width="3"/><path d="M10 15h10M15 10v10" stroke="var(--orange)" stroke-width="3"/></svg></div>
        <p class="biz-desc">건설현장 근로일수에 따라 적립된 퇴직공제금 지급</p>
      </article>
      <article class="biz-card">
        <div class="biz-name">무이자 생활안정자금 대부</div>
        <div class="biz-icon"><svg width="30" height="30" viewBox="0 0 30 30"><path d="M5 14 15 5l10 9v11H5Z" fill="none" stroke="var(--orange)" stroke-width="3"/></svg></div>
        <p class="biz-desc">생계비가 필요한 근로자에게 무이자로 생활자금 대부</p>
      </article>
      <article class="biz-card">
        <div class="biz-name">각종 복지서비스</div>
        <div class="biz-icon"><svg width="30" height="30" viewBox="0 0 30 30"><path d="M15 25 5 15a5 5 0 0 1 10-6 5 5 0 0 1 10 6Z" fill="var(--orange)"/></svg></div>
        <p class="biz-desc">결혼·출산 보조금, 자녀 교육비, 건강검진 지원</p>
      </article>
      <article class="biz-card">
        <div class="biz-name">무료 취업지원</div>
        <div class="biz-icon"><svg width="30" height="30" viewBox="0 0 30 30"><rect x="5" y="10" width="20" height="14" rx="2" fill="none" stroke="var(--orange)" stroke-width="3"/><path d="M11 10V6h8v4" fill="none" stroke="var(--orange)" stroke-width="3"/></svg></div>
        <p class="biz-desc">구인자와 구직자를 무료로 연결하는 취업지원</p>
      </article>
      <article class="biz-card">
        <div class="biz-name">건설기능향상 훈련지원</div>
        <div class="biz-icon"><svg width="30" height="30" viewBox="0 0 30 30"><path d="M15 26V12M15 14c-6 0-8-4-8-8 5 0 8 3 8 8M15 12c0-5 3-8 8-8 0 4-2 8-8 8" fill="none" stroke="var(--green-deep)" stroke-width="3"/></svg></div>
        <p class="biz-desc">숙련도를 높이는 기능훈련 과정 무료 운영</p>
      </article>
    </div>

    <footer class="footer">
      <div class="contact">
        <div><b>대표번호</b><span class="sep"></span>1600-4827</div>
        <div><b>홈페이지</b><span class="sep"></span>www.nurihoe.or.kr/hanul</div>
      </div>
      <div class="brand-foot"><span class="brand-dot"></span>푸른들누리회</div>
    </footer>
  </section>
</main>
</body>
</html>
```